BeLMoZ clinical trial results infographic

We need an infographic which presents the results from the BeLMoZ research trial. It should be colourful and engaging, in understandable language and showing the steps to get to the results. This is to showcase the results to patients/the public/clinicians, giving a brief summary of what the study proved. The final design should have the BeLMoZ logo at the top (please see the logo on the attached Word document)
I have attached the required logos which need to be used (BeLMoZ - within the Word doc, Pembury Injury and Urgent Care, University of Wrenford) as well as an example from another study, KWELLO3, as an example of what the layout could look like. Please DO NOT use the content from the KWELLO3 example though, please instead use the content from the attached document 'InfographicDesignInformation_BELMOZ_ArtPosse_02Dec2025'. Please also include information about the funding in a footer at the bottom of the infographic (as per the above document).

```html
<!DOCTYPE html>
<html lang="en">
<head>
<meta charset="utf-8">
<title>BeLMoZ – Study Results Infographic</title>
<link href="https://fonts.googleapis.com/css2?family=Poppins:wght@400;500;600;700;800&display=swap" rel="stylesheet">
<style>
  :root{
    --ink:#111111;
    --ink-soft:#3d3d3d;
    --band-dark:#8a8a8a;
    --band-light:#e3e3e3;
    --paper:#ffffff;
    --muted:#9a9a9a;
    --frame:#5b6b7c;
    --pill:#333333;
  }
  *{box-sizing:border-box;margin:0;padding:0}
  html,body{width:899px;height:1200px;overflow:hidden;background:var(--paper)}
  body{font-family:"Poppins",sans-serif;color:var(--ink)}
  .sheet{position:relative;width:899px;height:1200px;overflow:hidden;background:var(--paper)}

  .brand-name{position:absolute;left:73px;top:50px;font-size:46px;font-weight:700;letter-spacing:1px;color:var(--ink)}
  .uni-mark{position:absolute;left:730px;top:78px;display:flex;align-items:center;gap:7px;font-size:12px;font-weight:600;color:var(--ink)}
  .uni-mark .square{width:12px;height:12px;background:var(--ink)}

  .headline{position:absolute;left:40px;right:40px;top:142px;text-align:center;font-size:22.5px;line-height:27px;font-weight:700;color:var(--ink)}
  .headline .soft{color:var(--ink-soft)}

  .summary-band{position:absolute;left:0;top:200px;width:899px;height:292px}
  .summary-title{position:absolute;left:51px;top:292px;font-size:21px;font-weight:700;color:var(--paper)}
  .summary-text{position:absolute;left:51px;top:326px;width:575px;font-size:11.2px;line-height:14px;color:var(--paper)}
  .summary-visual{position:absolute;left:643px;top:272px;width:178px;height:178px;border-radius:50%;border:5px solid var(--paper);background:radial-gradient(circle at 40% 40%,#e2e2e2,#b4b4b4)}

  .key-title{position:absolute;left:50px;top:507px;font-size:21px;font-weight:700}
  .key-text{position:absolute;left:50px;top:541px;width:790px;font-size:11.6px;line-height:14px;color:var(--ink-soft)}

  .eligibility{position:absolute;left:52px;top:636px;width:795px;height:124px;border:1.3px solid var(--frame)}
  .eligibility-tab{position:absolute;left:332px;top:605px;width:234px;height:32px;background:var(--ink);color:var(--paper);font-size:20px;font-weight:700;text-align:center;line-height:33px;clip-path:polygon(4% 0,96% 0,100% 100%,0 100%)}
  .col{position:absolute;top:18px}
  .col.included{left:22px;width:330px}
  .col.excluded{left:413px;width:370px}
  .col-divider{position:absolute;left:393px;top:26px;height:92px;border-left:1.3px dashed var(--frame)}
  .col h3{font-size:15.5px;font-weight:700;color:var(--ink-soft);margin-bottom:6px}
  .col ul{list-style:none}
  .col li{position:relative;padding-left:19px;font-size:11.6px;line-height:13.5px;margin-bottom:12px}
  .col.included li{font-weight:700}
  .tick{position:absolute;left:0;top:2px;width:9px;height:9px}

  .details-band{position:absolute;left:0;top:776px;width:899px;height:254px;background:var(--band-light)}
  .details-title{position:absolute;left:52px;top:796px;font-size:21px;font-weight:700}
  .details-list{position:absolute;left:52px;top:830px;width:290px;list-style:none}
  .details-list li{position:relative;padding-left:25px;font-size:11.6px;line-height:14.4px;margin-bottom:14px;color:var(--ink-soft)}
  .details-list li b{color:var(--ink)}
  .details-list .tick{top:3px}
  .dash{position:absolute;top:821px;height:163px;border-left:1.3px dashed var(--ink-soft)}
  .hospital-visual{position:absolute;left:392px;top:826px;width:208px;height:142px;background:linear-gradient(180deg,#cfcfcf,#9c9c9c)}
  .hospital-label{position:absolute;left:392px;top:980px;width:156px;text-align:center;font-size:11px;line-height:14px;font-weight:700}
  .people-visual{position:absolute;left:662px;top:842px;width:158px;height:124px;background:linear-gradient(90deg,#a8a8a8 0%,#a8a8a8 30%,#1a1a1a 70%)}

  .funding{position:absolute;left:60px;right:60px;top:1064px;text-align:center;font-size:12.6px;line-height:17px;color:var(--ink-soft)}
  .contact-pill{position:absolute;left:49px;top:1137px;width:284px;height:70px;background:var(--pill);border-radius:16px 16px 0 0;color:var(--paper);font-size:11.6px;display:flex;align-items:flex-start;padding:17px 0 0 23px;gap:8px}
  .contact-pill svg{width:14px;height:11px;margin-top:3px}
  .partner-mark{position:absolute;left:378px;top:1150px;display:flex;align-items:center;gap:9px;font-size:18.5px;font-weight:400;color:#6f6f6f}
  .partner-mark .square{width:22px;height:22px;background:#8e8e8e}
</style>
</head>
<body>
<main class="sheet">

  <header>
    <div class="brand-name">BeLMoZ</div>
    <div class="uni-mark"><span class="square"></span>University of Wrenford</div>
    <h1 class="headline">IN OPERATIONS ON BROKEN LOWER THIGHS, SURGEONS USE<br><span class="soft">A NAIL OR A PLATE, AND A FUTURE STUDY COULD ESTABLISH<br>WHICH IMPLANT HAS BETTER OUTCOMES.</span></h1>
  </header>

  <section class="summary">
    <svg class="summary-band" viewBox="0 0 899 292" preserveAspectRatio="none" aria-hidden="true">
      <path d="M0 16 Q450 120 899 8 L899 292 L0 292 Z" fill="var(--band-dark)"/>
      <path d="M0 16 Q450 120 899 8 Q450 80 45 24 Z" fill="var(--ink)"/>
      <path d="M0 16 Q450 120 899 8 Q450 68 0 16 Z" fill="var(--paper)" opacity="0"/>
    </svg>
    <h2 class="summary-title">STUDY SUMMARY</h2>
    <p class="summary-text">Distal femur fractures (broken thighbone just above the knee) occur mostly in older patients after a fall, and in younger men during major trauma such as traffic accidents. In this feasibility study comparing the use of two surgical implants, half of the patients were treated with an intramedullary nail and half had an external locking plate. A lower number of patients was recruited than expected. A process evaluation helped to explain this: surgeons appeared to select the fitter patients for inclusion, and sometimes had a preference for either nail or plate; and variation in working practices between hospitals. Completion of data was also lower than expected and the process evaluation showed that already frail patients had difficulty with lengthy forms.</p>
    <div class="summary-visual" role="img" aria-label="Illustration of a knee joint just below the broken thighbone"></div>
  </section>

  <section class="key-messages">
    <h2 class="key-title">KEY MESSAGES</h2>
    <p class="key-text">A comparison study of nail versus plate in distal femur fractures is feasible, with simpler procedures and if the design can allow for surgeons’ preferences</p>
  </section>

  <section>
    <div class="eligibility-tab">ELIGIBILITY CRITERIA</div>
    <div class="eligibility">
      <div class="col included">
        <h3>INCLUDED</h3>
        <ul>
          <li><svg class="tick" viewBox="0 0 10 10"><circle cx="5" cy="5" r="5" fill="var(--ink)"/><path d="M2.6 5.1l1.6 1.6 3.2-3.3" stroke="#fff" stroke-width="1.3" fill="none"/></svg>Aged 18 and over</li>
          <li><svg class="tick" viewBox="0 0 10 10"><circle cx="5" cy="5" r="5" fill="var(--ink)"/><path d="M2.6 5.1l1.6 1.6 3.2-3.3" stroke="#fff" stroke-width="1.3" fill="none"/></svg>Fracture of the distal femur which the surgeon believed would benefit from internal fixation</li>
        </ul>
      </div>
      <div class="col-divider"></div>
      <div class="col excluded">
        <h3>EXCLUDED : PATIENTS WITH</h3>
        <ul>
          <li><svg class="tick" viewBox="0 0 10 10"><circle cx="5" cy="5" r="5" fill="var(--ink)"/><path d="M2.6 5.1l1.6 1.6 3.2-3.3" stroke="#fff" stroke-width="1.3" fill="none"/></svg>A loose knee or hip arthroplasty requiring revision</li>
          <li><svg class="tick" viewBox="0 0 10 10"><circle cx="5" cy="5" r="5" fill="var(--ink)"/><path d="M2.6 5.1l1.6 1.6 3.2-3.3" stroke="#fff" stroke-width="1.3" fill="none"/></svg>An arthroplasty or pre-existing femoral deformity that precluded nail fixation.</li>
        </ul>
      </div>
    </div>
  </section>

  <section>
    <div class="details-band"></div>
    <h2 class="details-title">STUDY DETAILS</h2>
    <ul class="details-list">
      <li><svg class="tick" viewBox="0 0 10 10"><circle cx="5" cy="5" r="5" fill="var(--ink)"/><path d="M2.6 5.1l1.6 1.6 3.2-3.3" stroke="#fff" stroke-width="1.3" fill="none"/></svg>A randomised controlled feasibility study at <b>seven Public hospitals</b> in <b>England. 23 of 82 eligible patients</b> were recruited <b>(nail, 11; plate, 12).</b></li>
      <li><svg class="tick" viewBox="0 0 10 10"><circle cx="5" cy="5" r="5" fill="var(--ink)"/><path d="M2.6 5.1l1.6 1.6 3.2-3.3" stroke="#fff" stroke-width="1.3" fill="none"/></svg>Participants were blinded to the allocation. Primary outcomes were recruitment rate and completion rate of <b>QL-5D</b> (Quality of life) <b>at 4 months after surgery.</b></li>
    </ul>
    <div class="dash" style="left:353px"></div>
    <div class="hospital-visual" role="img" aria-label="Illustration of a hospital building with trees"></div>
    <div class="hospital-label">SEVEN PUBLIC<br>HOSPITALS</div>
    <div class="dash" style="left:626px"></div>
    <div class="people-visual" role="img" aria-label="Ten person figures, three grey and seven black, showing recruited patients"></div>
  </section>

  <footer>
    <p class="funding">National Institute of Care Studies Health Technology Review (15/59/22), supported by the NICS Wrenford Biomedical Research Centre</p>
    <div class="contact-pill">
      <svg viewBox="0 0 14 11" aria-hidden="true"><rect x="0.6" y="0.6" width="12.8" height="9.8" fill="none" stroke="#fff" stroke-width="1.2"/><path d="M0.8 0.8L7 6l6.2-5.2" fill="none" stroke="#fff" stroke-width="1.2"/></svg>
      limbcare@wrenford-trials.org
    </div>
    <div class="partner-mark"><span class="square"></span>PEMBURY INJURY &amp; URGENT CARE</div>
  </footer>

</main>
</body>
</html>
```